Business Card, Stationary with Shark Logo for Personal Injury Lawyer

I need business cards and stationery with a shark logo for my Personal Injury Law Practice. Has to have this written on it:
Martin K. Hollis
Injury Lawyer
The Corvell Building
718 Tandy Street
Providence, Rhode Island 02908
401-627-4193
Martinhollis.com

Contact Information for Business Card

Martin K. Hollis, Injury Lawyer, address, 401-627-4193, martinhollis.com

```html
<!DOCTYPE html>
<html lang="en">
<head>
<meta charset="utf-8">
<title>Martin K. Hollis – Business Card</title>
<link rel="stylesheet" href="https://fonts.googleapis.com/css2?family=Montserrat:wght@400;700;800&family=Open+Sans:wght@400&display=swap">
<style>
  :root {
    --navy: #2b2766;
    --paper: #ffffff;
    --backdrop: #e9e9ec;
    --muted: #8c8c92;
    --rule: #2b2766;
  }
  * { margin: 0; padding: 0; box-sizing: border-box; }
  html, body {
    width: 1200px;
    height: 800px;
    overflow: hidden;
    background: var(--backdrop);
  }
  .canvas {
    position: relative;
    width: 1200px;
    height: 800px;
  }
  .card {
    position: absolute;
    left: 300px;
    width: 600px;
    height: 343px;
    background: var(--paper);
    overflow: hidden;
    box-shadow: 0 6px 20px rgba(0,0,0,0.12);
  }
  .card--front { top: 36px; }
  .card--back { top: 421px; }

  .pattern-area {
    position: absolute;
  }
  .card--front .pattern-area {
    right: 0;
    top: 0;
    width: 250px;
    height: 100%;
    background: radial-gradient(ellipse 100% 95% at 100% 65%, var(--navy) 0%, rgba(43,39,102,0.6) 40%, rgba(43,39,102,0) 100%);
  }
  .card--back .pattern-area {
    left: 0;
    top: 0;
    width: 340px;
    height: 230px;
    background: radial-gradient(ellipse 100% 100% at 0% 0%, var(--navy) 0%, rgba(43,39,102,0.6) 40%, rgba(43,39,102,0) 100%);
  }

  .brand {
    position: absolute;
    display: flex;
    align-items: center;
    gap: 10px;
  }
  .brand__mark {
    width: 14px;
    height: 14px;
    background: var(--navy);
    flex: none;
  }
  .brand__name {
    font-family: 'Montserrat', sans-serif;
    font-weight: 800;
    color: var(--navy);
    text-transform: uppercase;
    letter-spacing: 0.5px;
    line-height: 1.05;
  }
  .card--front .brand {
    left: 44px;
    top: 36px;
  }
  .card--front .brand__name { font-size: 26px; }
  .card--back .brand {
    right: 44px;
    bottom: 56px;
  }
  .card--back .brand__name { font-size: 30px; }

  .identity {
    position: absolute;
    left: 58px;
    top: 128px;
    padding-left: 12px;
    border-left: 2px solid var(--rule);
  }
  .identity__name {
    font-family: 'Montserrat', sans-serif;
    font-weight: 700;
    font-size: 19px;
    color: var(--navy);
    text-transform: uppercase;
    letter-spacing: 0.5px;
  }
  .identity__title {
    font-family: 'Montserrat', sans-serif;
    font-weight: 400;
    font-size: 13px;
    color: var(--muted);
    letter-spacing: 0.8px;
    margin-top: 2px;
  }

  .contact {
    position: absolute;
    left: 66px;
    bottom: 26px;
    width: 270px;
    list-style: none;
    font-family: 'Open Sans', sans-serif;
    font-size: 12px;
    line-height: 16px;
    color: var(--muted);
    letter-spacing: 0.2px;
  }
  .contact__item {
    display: flex;
    align-items: flex-start;
    gap: 8px;
    margin-top: 5px;
  }
  .contact__icon {
    width: 13px;
    height: 13px;
    margin-top: 1.5px;
    flex: none;
  }
</style>
</head>
<body>
<main class="canvas">

  <section class="card card--front" aria-label="Business card front">
    <div class="brand">
      <span class="brand__mark" aria-hidden="true"></span>
      <span class="brand__name">Martin K.<br>Hollis</span>
    </div>

    <div class="identity">
      <p class="identity__name">Martin K. Hollis</p>
      <p class="identity__title">Injury Lawyer</p>
    </div>

    <ul class="contact">
      <li class="contact__item">
        <svg class="contact__icon" viewBox="0 0 14 14" aria-hidden="true">
          <circle cx="7" cy="7" r="7" fill="#2b2766"/>
          <path d="M4.6 3.6 L6 3.6 L6.6 5.4 L5.7 6.1 Q6.5 7.8 7.9 8.3 L8.6 7.4 L10.4 8 L10.4 9.4 Q10.4 10.4 9.4 10.4 Q4.2 10 3.6 4.6 Q3.6 3.6 4.6 3.6 Z" fill="#fff"/>
        </svg>
        <span>401-627-4193</span>
      </li>
      <li class="contact__item">
        <svg class="contact__icon" viewBox="0 0 14 14" aria-hidden="true">
          <circle cx="7" cy="7" r="7" fill="#2b2766"/>
          <path d="M7 11 Q4 7.6 4 5.8 A3 3 0 0 1 10 5.8 Q10 7.6 7 11 Z" fill="#fff"/>
          <circle cx="7" cy="5.8" r="1.1" fill="#2b2766"/>
        </svg>
        <span>The Corvell Building, 718 Tandy Street<br>Providence, Rhode Island 02908</span>
      </li>
      <li class="contact__item">
        <svg class="contact__icon" viewBox="0 0 14 14" aria-hidden="true">
          <circle cx="7" cy="7" r="7" fill="#2b2766"/>
          <rect x="3.5" y="4.5" width="7" height="5" fill="none" stroke="#fff" stroke-width="0.9"/>
          <path d="M3.5 4.5 L7 7.4 L10.5 4.5" fill="none" stroke="#fff" stroke-width="0.9"/>
        </svg>
        <span>martin@martinhollis.com</span>
      </li>
      <li class="contact__item">
        <svg class="contact__icon" viewBox="0 0 14 14" aria-hidden="true">
          <circle cx="7" cy="7" r="7" fill="#2b2766"/>
          <circle cx="7" cy="7" r="4" fill="none" stroke="#fff" stroke-width="0.8"/>
          <ellipse cx="7" cy="7" rx="1.8" ry="4" fill="none" stroke="#fff" stroke-width="0.8"/>
          <line x1="3" y1="7" x2="11" y2="7" stroke="#fff" stroke-width="0.8"/>
        </svg>
        <span>www.Martinhollis.com</span>
      </li>
    </ul>

    <div class="pattern-area" role="img" aria-label="Navy triangle mosaic pattern fading out toward the centre"></div>
  </section>

  <section class="card card--back" aria-label="Business card back">
    <div class="pattern-area" role="img" aria-label="Navy triangle mosaic pattern fading out from the top left corner"></div>
    <div class="brand">
      <span class="brand__mark" aria-hidden="true"></span>
      <span class="brand__name">Martin K.<br>Hollis</span>
    </div>
  </section>

</main>
</body>
</html>
```